We need a full website with logo/graphics/woocommerce for hemp-based company

This site will be velmorix.com. It is a website featuring the fact we are the only manufacturer to produce CBDP and THCP. It should be great on mobile and desktop. We will pay for any extensions needed and while it should be a simple site:

About Us
About the Laboratory
About CBDP
About THCP
Shop
Contact Us

Only 4 products on the site.

It can be wordpress or joomla. Your choice. You must install the final website on our server. We agree to pay for monthly support that must be submitted in your quote.

He have a great graphics designer that will assist keeping colors and graphics clean according to your specifications.

Industry/Entity Type

Hemp CBD THC

Coding

Coded - Design and coding required

Number of Pages Required

5+ page

Requirements
Must have
• A simple clean layout

```html
<!DOCTYPE html>
<html lang="en">
<head>
<meta charset="utf-8">
<title>Velmorix — The Next Revolution in Cannabinoids</title>
<link rel="stylesheet" href="https://fonts.googleapis.com/css2?family=Pirata+One&family=Great+Vibes&family=Roboto:wght@400;500;700&display=swap">
<style>
:root{
  --green:#2ef26f;
  --green-dark:#1e9a5c;
  --ink:#1a1a1a;
  --text:#666;
  --line:#e3e3e3;
  --footer:#1f1f1f;
  --white:#fff;
}
*{margin:0;padding:0;box-sizing:border-box}
html,body{width:1200px;height:3507px;overflow:hidden;background:var(--white)}
body{position:relative;font-family:"Roboto",sans-serif;color:var(--ink)}
.abs{position:absolute}
.display{font-family:"Pirata One",serif;font-weight:400;letter-spacing:1px;color:var(--ink)}
.para{font-size:12.5px;line-height:27.2px;color:var(--text)}
.btn{position:absolute;display:flex;align-items:center;justify-content:center;background:var(--green);color:var(--white);border-radius:40px;font-weight:500;font-size:16px;text-transform:uppercase}

/* header */
.site-header{left:0;top:0;width:1200px;height:113px;border-bottom:1px solid var(--line)}
.brand{display:flex;align-items:center;gap:8px}
.brand span{font-family:"Roboto",sans-serif;font-weight:700;font-size:22px;color:var(--ink)}
.brand i{display:block;width:16px;height:16px;border-radius:50%;background:var(--green-dark)}
.brand-top{left:145px;top:38px}
.brand-foot{left:164px;top:108px}
.brand-foot span{color:var(--white);font-size:24px}
.search{left:681px;top:19px;width:263px;height:39px;border:1px solid #cfcfcf;display:flex;align-items:center;padding-left:18px;font-size:11px;color:#777}
.search-btn{position:absolute;right:2px;top:2px;width:32px;height:33px;background:var(--green-dark);display:flex;align-items:center;justify-content:center}
.nav{left:360px;top:81px;display:flex;gap:24px;font-size:12.5px;font-weight:500;text-transform:uppercase}
.cart-badge{left:1038px;top:19px;width:15px;height:15px;border-radius:50%;background:var(--green-dark);color:#fff;font-size:9px;display:flex;align-items:center;justify-content:center}

/* hero */
.hero{left:0;top:113px;width:1200px;height:563px;background:radial-gradient(ellipse at 75% 40%,#b8d86a 0%,#5fa52f 35%,#2f6d1c 75%,#1d4a12 100%)}
.hero-title{left:143px;top:210px;font-size:78px;color:var(--white)}
.hero-script{left:143px;top:330px;font-family:"Great Vibes",cursive;font-size:54px;line-height:62px;color:var(--white)}
.dots{left:1124px;top:346px;display:flex;flex-direction:column;gap:13px}
.dots i{width:9px;height:9px;border-radius:50%;background:var(--white)}
.dots i.on{background:var(--green-dark)}

/* sections */
.photo{position:absolute}
.lab-card{left:143px;top:1323px;width:513px;height:472px;background:var(--white);box-shadow:0 0 18px rgba(0,0,0,.12)}
.divider{left:143px;top:2634px;width:912px;height:1px;background:var(--line)}

/* products */
.product{position:absolute;top:2833px;width:218px;height:257px;border:1px solid #dcdcdc}
.product .shot{position:absolute;left:30px;top:12px;width:156px;height:150px}
.product h3{position:absolute;left:0;top:180px;width:100%;text-align:center;font-size:14px;font-weight:700}
.product p{position:absolute;left:0;top:207px;width:100%;text-align:center;font-size:12px;color:var(--text)}
.product .btn{left:44px;top:235px;width:130px;height:43px;font-size:12.5px}

/* footer */
.site-footer{left:0;top:3188px;width:1200px;height:319px;background:var(--footer);color:#e6e6e6}
.f-head{font-size:15px;font-weight:700;color:var(--green)}
.f-links{font-size:11.5px;line-height:27px;color:#ddd}
.email{left:713px;top:143px;width:322px;height:44px;background:var(--white);border-radius:30px;color:#333;font-size:11px;display:flex;align-items:center;padding-left:30px}
.email .btn{left:auto;right:0;top:0;width:130px;height:44px;font-size:12.5px}
.pay{top:270px;width:31px;height:20px;border-radius:3px;background:#d5d9e0}
.social{top:273px;width:14px;height:14px;border-radius:50%;background:#fff}
</style>
</head>
<body>

<header class="abs site-header">
  <div class="abs brand brand-top"><i></i><span>Velmorix</span></div>
  <div class="abs search">Search..
    <div class="search-btn"><svg width="14" height="14" viewBox="0 0 14 14"><circle cx="6" cy="6" r="4.2" fill="none" stroke="#fff" stroke-width="1.8"/><line x1="9" y1="9" x2="12.5" y2="12.5" stroke="#fff" stroke-width="2"/></svg></div>
  </div>
  <svg class="abs" style="left:970px;top:22px" width="30" height="32" viewBox="0 0 30 32"><circle cx="15" cy="10" r="7" fill="none" stroke="#222" stroke-width="2"/><path d="M3 30c0-8 5-11 12-11s12 3 12 11z" fill="none" stroke="#222" stroke-width="2"/></svg>
  <svg class="abs" style="left:1012px;top:24px" width="34" height="30" viewBox="0 0 34 30"><path d="M1 3h6l4 17h17l3-12H9" fill="none" stroke="#222" stroke-width="2"/><circle cx="13" cy="26" r="2.5" fill="none" stroke="#222" stroke-width="2"/><circle cx="25" cy="26" r="2.5" fill="none" stroke="#222" stroke-width="2"/></svg>
  <div class="abs cart-badge">0</div>
  <nav class="abs nav"><span>Home</span><span>About Us</span><span>About the Laboratory</span><span>About CBDP</span><span>About THCP</span><span>Shop</span><span>Contact Us</span></nav>
</header>

<section class="abs hero" role="img" aria-label="Hemp leaves with an oil dropper over an amber bottle"></section>
<h1 class="abs display hero-title">Velmorix</h1>
<div class="abs hero-script">The Next Revolution<br>in Cannabinoids</div>
<a class="btn" style="left:143px;top:490px;width:194px;height:65px">Get Started</a>
<div class="abs dots"><i></i><i></i><i class="on"></i><i></i><i></i></div>

<!-- about us -->
<div class="abs" style="left:89px;top:744px;width:440px;height:440px;border-radius:50%;background:var(--green-dark)"></div>
<div class="photo" role="img" aria-label="Gloved hands holding a hemp leaf and an oil bottle over test tubes" style="left:110px;top:744px;width:420px;height:420px;border-radius:50%;background:radial-gradient(circle at 50% 40%,#f4f6f4,#d9dfe0 60%,#c9c77a 100%)"></div>
<h2 class="abs display" style="left:584px;top:755px;font-size:60px">About Us</h2>
<p class="abs para" style="left:584px;top:851px;width:470px">Lorem ipsum dolor sit amet, consectetur adipiscing elit, sed do eiusmod tempor incididunt ut labore et dolore magna aliqua. Quis ipsum suspendisse ultrices gravida. Risus commodo viverra maecenas accumsan lacus vel facilisisorem ipsum dolor sit amet, consectetur adipiscing elit, sed do eiusmod tempocididunt ut labore et dolore magna aliquauis ipsum suspendisse ultrices gravidasummodo viverra maecenas accumsan lacus vel facilisisrem ipsum dolor sit amconsectetur adipiscing elit, sed do eiusmod tempor incididunt ut labore et dolore maaliqua. Quis ipsum suspendisse ultrices gravs commodo viverra</p>
<a class="btn" style="left:584px;top:1101px;width:166px;height:56px">Read More</a>

<!-- laboratory -->
<div class="photo" role="img" aria-label="Scientist reading a tablet beside laboratory equipment" style="left:600px;top:1275px;width:600px;height:568px;background:linear-gradient(120deg,#d3d6e8,#b7bdd6 50%,#dfe1ea)"></div>
<div class="abs lab-card"></div>
<h2 class="abs display" style="left:204px;top:1362px;font-size:58px;line-height:54px">About the<br>Laboratory</h2>
<p class="abs para" style="left:204px;top:1496px;width:420px">Lorem ipsum dolor sit amet, consectetur adipiscing elit, sed do eiusmod tempor incididunt ut labore et dolore magna aliquais ipsum suspendisse ultrices gravida. Risus commodo viverra maecenas accumsan lacus vel facilisisorem ipsum dolor sit ame, consectetur adipiscing el do eiusmod tempocididunt ut labore et dolore magna aliquauis ipsum suspendisse ultrices gravidasummodo viverra maecenas accumsan</p>
<a class="btn" style="left:204px;top:1691px;width:166px;height:55px">Read More</a>

<!-- cbdp / thcp -->
<div class="photo" role="img" aria-label="Hemp leaves with molecule diagram and oil dropper" style="left:11px;top:1857px;width:579px;height:303px;background:linear-gradient(110deg,#1f3a14,#3d6a22 45%,#8a6a2a 80%,#2a2010)"></div>
<div class="photo" role="img" aria-label="Amber oil bottles and hemp leaves on dark wood" style="left:610px;top:1857px;width:580px;height:303px;background:linear-gradient(180deg,#2a2a2a,#3b3b3b 60%,#2d4a1e)"></div>
<h2 class="abs display" style="left:64px;top:2210px;font-size:58px">About CBDP</h2>
<p class="abs para" style="left:64px;top:2288px;width:420px">Lorem ipsum dolor sit amet, consectetur adipiscing elit, sed do eiusmod tempor incididunt ut labore et dolore magna aliquais ipsum suspendisse ultrices gravida. Risus commodo viverra maecenas accumsan lacus vel facilisisorem ipsum dolor sit ame, consectetur adipiscing el do eiusmod tempocididunt ut labore et dolore magna aliquauis ipsum suspendisse ultrices gravidasummodo viverra maecenas accumsan</p>
<a class="btn" style="left:64px;top:2482px;width:166px;height:56px">Read More</a>
<h2 class="abs display" style="left:664px;top:2210px;font-size:58px">About THCP</h2>
<p class="abs para" style="left:664px;top:2288px;width:420px">Lorem ipsum dolor sit amet, consectetur adipiscing elit, sed do eiusmod tempor incididunt ut labore et dolore magna aliquais ipsum suspendisse ultrices gravida. Risus commodo viverra maecenas accumsan lacus vel facilisisorem ipsum dolor sit ame, consectetur adipiscing el do eiusmod tempocididunt ut labore et dolore magna aliquauis ipsum suspendisse ultrices gravidasummodo viverra maecenas accumsan</p>
<a class="btn" style="left:664px;top:2482px;width:166px;height:56px">Read More</a>

<div class="abs divider"></div>

<!-- shop -->
<h2 class="abs display" style="left:0;top:2718px;width:1200px;text-align:center;font-size:60px">Shop Products</h2>
<div class="product" style="left:143px"><div class="shot" role="img" aria-label="Black vape pen" style="background:linear-gradient(90deg,#fff 38%,#1a1a1a 38%,#333 62%,#fff 62%)"></div><h3>Product Name</h3><p>$56.98</p><a class="btn">Shop Now</a></div>
<div class="product" style="left:375px"><div class="shot" role="img" aria-label="Pile of gummy bears" style="background:radial-gradient(ellipse at 50% 55%,#f2b829 0%,#e6522d 40%,#fff 70%)"></div><h3>Product Name</h3><p>$56.98</p><a class="btn">Shop Now</a></div>
<div class="product" style="left:607px"><div class="shot" role="img" aria-label="Glass flask of oil with hemp leaf" style="background:radial-gradient(circle at 55% 60%,#f0c81c 0%,#e8d26a 30%,#fff 62%)"></div><h3>Product Name</h3><p>$56.98</p><a class="btn">Shop Now</a></div>
<div class="product" style="left:839px"><div class="shot" role="img" aria-label="Oil bottle with hemp leaf" style="background:radial-gradient(circle at 50% 60%,#e9c20a 0%,#5c9a1e 35%,#fff 65%)"></div><h3>Product Name</h3><p>$56.98</p><a class="btn">Shop Now</a></div>

<!-- footer -->
<footer class="abs site-footer">
  <div class="abs brand brand-foot"><i></i><span>Velmorix</span></div>
  <div class="abs f-head" style="left:385px;top:55px">Quick Links</div>
  <div class="abs f-links" style="left:385px;top:96px">Home<br>About Us<br>About the Laboratory<br>About CBDP</div>
  <div class="abs f-links" style="left:544px;top:96px">About THCP<br>Shop<br>Contact Us</div>
  <div class="abs f-head" style="left:713px;top:55px">Sign Up Newsletter</div>
  <div class="abs f-links" style="left:713px;top:96px">Lorem ipsum dolor sit amet consectetur adipiscing elit,</div>
  <div class="abs email">Enter Email<a class="btn">Subscribe</a></div>
  <div class="abs" style="left:164px;top:273px;font-size:11.5px;color:#ddd">© Velmorix 2021. All Rights Reserved &nbsp;|&nbsp; Privacy Policy &nbsp;|&nbsp; Terms and Use</div>
  <div class="abs pay" style="left:663px"></div>
  <div class="abs pay" style="left:703px"></div>
  <div class="abs pay" style="left:743px"></div>
  <div class="abs pay" style="left:783px"></div>
  <div class="abs pay" style="left:823px"></div>
  <div class="abs social" style="left:958px"></div>
  <div class="abs social" style="left:987px"></div>
  <div class="abs social" style="left:1018px"></div>
</footer>

</body>
</html>
```